Documentary Film: DVD Box Set - Cover Design

We have an old DVD Cover Design from the first film we produced in 2010, called 'Kōpūrehu te Rangiwhākoro'.

In 2020, we released our second film, 'Hekereri'.

People still want DVD copies of our films which are now streaming online, so we figured, the best thing to do was release BOTH films as a DVD BOX SET.

We'd like you to design a new DVD Cover (for both films together) including compatible DVD face labels, (one for each film which will be sold as separate discs inside the box set).

Target Market(s)

Local residents and older generations are interested in our project.
Our film is screening on National Television in New Zealand, so must be of professional quality.
Eventually, the film will be sold online and in Library/ Museum gift store display cases.

Industry/Entity Type

Film Production

Font styles to use
Script

Requirements
Must have
• 2010 Film - 'Kōpūrehu te Rangiwhākoro'. We would like to stick with something similar to the original cover design (attached), with the updated cover blurb (included in the first design brief, attached).

2020 Film - 'Hekereri'. We invite you to develop the cover design for the new film and integrate it with the previous 2010 film as a box set as you see fit. (Wording to be included is provided in the second design brief, attached).

The DVD Dust Cover and DVD Face Labels must be sized in accordance with our DVD printer's design specifications (attached).

While we'd like the designs for both films to be compatible, it should be clear they are separate productions. 'Hekereri' is the primary focus, with 'Kōpūrehu te Rangiwhākoro' being the BONUS CONTENT.

The Project LOGO included in the second design brief (attached) should be included on the Back Cover. PLEASE USE THE SAME FONT AS USED IN THE PROJECT LOGO.

We must include ALL sponsor logos from both the original 2010 Film and the new 2020 film (logos attached). These do not need to be prominent in the design and can be reordered, resized or combined as appropriate.

There is a lot of New Zealand Māori in these design briefs, so please watch the macrons. Thank you.
Nice to have
• I would like the design for the new 2020 to match the style/ general of the film's website and Plinthra pages: Website: https://hekererifilm.com/ Plinthra: https://plinthra.tv/ondemand/h3kereri ; however, the designer has full license over how the new film's cover will look and feel.
(If we can build the box set cover first, we may come back to release just the second film by itself, as a separate project).
The traditional tattoo "Ta Moko" motif (or an abstract version of) may be used as backdrop imagery
Should not have
• No Polynesian or Celtic designs, please. This is strictly a New Zealand Māori production.

```html
<!DOCTYPE html>
<html lang="en">
<head>
<meta charset="utf-8">
<title>Hekereri – Disc Label</title>
<link rel="stylesheet" href="https://fonts.googleapis.com/css2?family=Parisienne&family=Source+Code+Pro:wght@400&family=Arimo:wght@400&display=swap">
<style>
  :root {
    --page: #ffffff;
    --shadow-deep: #120d0b;
    --shadow-warm: #2a1e19;
    --blanket-grey: #6f655d;
    --blanket-light: #958a80;
    --ember: #b0583a;
    --rim-shade: #1a1411;
    --motif-shade: #0c0908;
    --hole: #000000;
    --title-green: #8a9a5b;
    --credit-grey: #a49e98;
    --credit-edge: #231b17;
    --year-tan: #cbbcae;
  }
  * { margin: 0; padding: 0; box-sizing: border-box; }
  html, body {
    width: 1200px;
    height: 1187px;
    overflow: hidden;
    background: var(--page);
  }
  .disc-label {
    position: relative;
    width: 1200px;
    height: 1187px;
  }
  .disc-art { position: absolute; inset: 0; display: block; }
  .credits-ring {
    font-family: "Source Code Pro", monospace;
    font-size: 22px;
    fill: var(--credit-grey);
    stroke: var(--credit-edge);
    stroke-width: 2.5px;
    stroke-opacity: 0.55;
    paint-order: stroke fill;
  }
  .film-title {
    font-family: "Parisienne", cursive;
    font-size: 225px;
    fill: var(--title-green);
  }
  .release-year {
    font-family: "Arimo", sans-serif;
    font-size: 36px;
    fill: var(--year-tan);
  }
</style>
</head>
<body>
<main class="disc-label">
  <svg class="disc-art" width="1200" height="1187" viewBox="0 0 1200 1187" xmlns="http://www.w3.org/2000/svg">
    <defs>
      <linearGradient id="scene-tone" x1="0.85" y1="0.1" x2="0.15" y2="0.95">
        <stop offset="0" stop-color="var(--shadow-deep)"/>
        <stop offset="0.4" stop-color="var(--shadow-warm)"/>
        <stop offset="0.75" stop-color="var(--blanket-grey)"/>
        <stop offset="1" stop-color="var(--blanket-light)"/>
      </linearGradient>
      <radialGradient id="ember-glow" cx="0.72" cy="0.88" r="0.28">
        <stop offset="0" stop-color="var(--ember)" stop-opacity="0.7"/>
        <stop offset="1" stop-color="var(--ember)" stop-opacity="0"/>
      </radialGradient>
      <radialGradient id="rim-vignette" cx="0.5" cy="0.5" r="0.5">
        <stop offset="0.8" stop-color="var(--rim-shade)" stop-opacity="0"/>
        <stop offset="1" stop-color="var(--rim-shade)" stop-opacity="0.6"/>
      </radialGradient>
      <radialGradient id="motif-fade" cx="0.5" cy="0.5" r="0.5">
        <stop offset="0" stop-color="var(--motif-shade)" stop-opacity="0.45"/>
        <stop offset="0.8" stop-color="var(--motif-shade)" stop-opacity="0.3"/>
        <stop offset="1" stop-color="var(--motif-shade)" stop-opacity="0"/>
      </radialGradient>
      <path id="credit-path" d="M133,920 A570,570 0 0,1 1067,266 A570,570 0 0,1 974,1033"/>
    </defs>

    <g class="disc-photo" role="img" aria-label="Film still: a young Māori woman with moko kauae, wrapped in a grey plaid blanket beside a fire">
      <circle cx="600" cy="593" r="593" fill="url(#scene-tone)"/>
      <circle cx="600" cy="593" r="593" fill="url(#ember-glow)"/>
    </g>

    <ellipse class="motif-watermark" role="img" aria-label="Faint tā moko koru motif as backdrop decoration"
             cx="815" cy="360" rx="150" ry="215" transform="rotate(38 815 360)" fill="url(#motif-fade)"/>

    <circle class="rim-vignette" cx="600" cy="593" r="593" fill="url(#rim-vignette)"/>

    <text class="credits-ring">
      <textPath href="#credit-path" textLength="2632" lengthAdjust="spacing">Director/ Producer: Mereana Holt - Writer/ Assistant Director: Tane Whitcombe - Executive Producer: Aroha Benton - Associate Producer: Rawiri Benton - Editor: Celeste Marchand - Director of Photography: Hemi Talbot</textPath>
    </text>

    <circle class="spindle-hole" cx="606" cy="600" r="106" fill="var(--hole)"/>

    <text class="film-title" x="600" y="905" text-anchor="middle">Hekereri</text>
    <text class="release-year" x="598" y="995" text-anchor="middle">©2020</text>
  </svg>
</main>
</body>
</html>
```